" O escritório Brunoro Arquitetura desenvolve projetosarquitetônicos e interiores, além de acompanhamento e administraçãao de obras. Tem a frente de sua gestão a arquiteta Mariana Forteso, que prioriza o atendimento exclusivo e diferenciado a cada um dos clientes, estabelecendo assim uma relação de proximidade, confiança e fidelização. Todos os projetos são desenvolvidos de acordo com o perfil do cliente, buscando sempre soluções inovadoras, criativas e acessíveis, em muitos casos utilizando materiais e soluções alternativas ao convencional, marca do escritório. O espaço físico do escritório reflete essa proposta de inovação e criatividade, que permite a acessibilidade da arquitetura a qualquer pessoa, desmistificando o status de que a boa arquitetura é acessível somente àqueles que possuem um alto poder aquisitivo. Todo o processo de concepção e posterior execução dos trabalhos é realizada entre os profissionais envolvidos e os clientes com total transparência, sendo a política de trabalho do escritório focada na ética, honestidade e respeito ao cliente, não havendo portanto o recebimento de reservas técnicas ou comissões de lojistas e empresas terceiras, para indicação de produtos. Assim, trabalhamos com total liberdade na concepção e especificação de materiais e soluções nos projetos. O escritório também tem ligação forte com as escolas de arquitetura da cidade, sendo um local de estágio e constante aprendizado para estudantes, que adquirem experiência profissional junto aos membros do escritório. A linguagem dos projetos, que deve se refletir na identidade visual da marca, busca a simplicidade dos materiais e formas, aplicadas da forma correta, gerando resultados simples, porém sofisticados. Priorizamos o uso dos materiais naturais em todos os projetos, mas prioritariamente o uso da madeira natural. Trabalhamos sempre com muito respeito pela história dos lugares, procurando sempre que possível preservar características originais que dão identidade aos lugares. "

```html
<!DOCTYPE html>
<html lang="pt-BR">
<head>
<meta charset="utf-8">
<title>Brunoro Arquitetura — Papel Timbrado</title>
<link rel="stylesheet" href="https://fonts.googleapis.com/css2?family=Montserrat:wght@300;400&family=Arimo:wght@400&display=swap">
<style>
  :root {
    --backdrop: #d6d6d6;
    --paper: #ffffff;
    --ink: #4a4a4a;
    --ink-soft: #7a7a7a;
    --ink-faint: #a8a8a8;
    --rule: #cfcfcf;
  }
  * { box-sizing: border-box; margin: 0; padding: 0; }
  html, body {
    width: 1200px; height: 1200px; overflow: hidden;
    background: var(--backdrop);
  }
  .letterhead {
    position: absolute;
    left: 207px; top: 50px;
    width: 786px; height: 1100px;
    background: var(--paper);
    border: 1px solid var(--rule);
    color: var(--ink);
  }
  .brand {
    position: absolute; top: 150px; left: 0; right: 0;
    text-align: center;
    font-family: "Montserrat", sans-serif;
    font-weight: 300;
    font-size: 26px;
    letter-spacing: 6px;
    text-transform: uppercase;
    color: var(--ink);
  }
  .brand-web {
    position: absolute; top: 208px; left: 0; right: 0;
    text-align: center;
    font-family: "Montserrat", sans-serif;
    font-weight: 400;
    font-size: 14px;
    color: var(--ink-soft);
  }
  .letter-body {
    position: absolute; top: 300px; left: 63px; right: 63px;
    font-family: "Arimo", sans-serif;
    font-size: 11px;
    line-height: 15px;
    color: var(--ink-soft);
    text-align: justify;
  }
  .letter-body p + p { margin-top: 15px; }
  .contact {
    position: absolute; left: 63px; top: 955px;
    font-family: "Arimo", sans-serif;
    font-size: 9.5px;
    line-height: 13px;
    color: var(--ink-soft);
  }
  .contact .phones { margin-top: 12px; }
  .signature {
    position: absolute; left: 580px; top: 955px;
    width: 80px; height: 55px;
    background: linear-gradient(180deg, #f4f4f4, #e9e9e9);
  }
  .seal {
    position: absolute; left: 670px; top: 950px;
    width: 68px; height: 68px;
  }
</style>
</head>
<body>
  <main class="letterhead">
    <h1 class="brand">Brunoro Arquitetura</h1>
    <p class="brand-web">www.brunoro.com.br</p>

    <section class="letter-body">
      <p>Lorem ipsum dolor sit amet, consectetur adipiscing elit. In ac magna tellus. Ut pretium faucibus quam, eu porttitor enim condimentum in. Mauris ac erat ac magna pellentesque aliquam. Donec consectetur, lectus eget eleifend commodo, augue purus tincidunt tortor, et vulputate urna magna non mauris. Integer nisl quam, mollis quis aliquet non, eleifend molestie dolor. Nulla at dolor nibh. Duis condimentum ornare vehicula. Integer velit nisi, dapibus cursus tincidunt nec, porttitor eu purus.</p>
      <p>Sed sodales commodo eros quis mollis. Duis convallis ante vel urna laoreet ultricies. Fusce eget suscipit massa. Quisque ultricies quam ut nulla porttitor non tempus lectus congue. Praesent id eros ut metus pulvinar sodales vel nec elit. Sed viverra elementum dui, quis faucibus purus tincidunt id. Curabitur felis metus, varius vitae euismod ut, ullamcorper quis justo. Nullam lobortis elit in lectus aliquet ornare. Maecenas euismod placerat est, a auctor neque malesuada ac. Aenean ut orci augue, sed egestas arcu.</p>
      <p>Vestibulum varius vestibulum molestie. Phasellus eu est sed elit ornare facilisis. Nullam ac urna ultricies ante ultricies adipiscing. Fusce nec velit nec arcu placerat tincidunt at id nibh. Suspendisse porttitor arcu eu mauris semper ac molestie dui convallis. Mauris vitae dolor massa, vel tristique nisi. Phasellus in turpis eu lorem suscipit lobortis id ut neque. Duis ac est a tellus egestas lacinia. Aenean scelerisque lacinia diam, vel tincidunt ipsum dignissim sed. Vivamus a ipsum in lacus faucibus placerat a sit amet ipsum. Vivamus scelerisque posuere erat, eget ornare magna consectetur ut. Morbi urna lorem, malesuada vitae egestas sit amet, auctor sit amet odio. Proin non nisl ligula.</p>
      <p>Sed sodales commodo eros quis mollis. Duis convallis ante vel urna laoreet ultricies. Fusce eget suscipit massa. Quisque ultricies quam ut nulla porttitor non tempus lectus congue. Praesent id eros ut metus pulvinar sodales vel nec elit. Sed viverra elementum dui, quis faucibus purus tincidunt id. Curabitur felis metus, varius vitae euismod ut, ullamcorper quis justo. Nullam lobortis elit in lectus aliquet ornare. Maecenas euismod placerat est, a auctor neque malesuada ac. Aenean ut orci augue, sed egestas arcu.</p>
      <p>Vestibulum varius vestibulum molestie. Phasellus eu est sed elit ornare facilisis. Nullam ac urna ultricies ante ultricies adipiscing. Fusce nec velit nec arcu placerat tincidunt at id nibh. Suspendisse porttitor arcu eu mauris semper ac molestie dui convallis. Mauris vitae dolor massa, vel tristique nisi. Phasellus in turpis eu lorem suscipit lobortis id ut neque. Duis ac est a tellus egestas lacinia. Aenean scelerisque lacinia diam, vel tincidunt ipsum dignissim sed. Vivamus a ipsum in lacus faucibus placerat a sit amet ipsum. Vivamus scelerisque posuere erat, eget ornare magna consectetur ut. Morbi urna lorem, malesuada vitae egestas sit amet, auctor sit amet odio. Proin non nisl ligula.</p>
    </section>

    <address class="contact">
      <p>Rua das Acácias, 480</p>
      <p>Bairro Jardim | CEP 04512-310</p>
      <p>São Paulo/SP</p>
      <p class="phones">Telefones: (11) 3456-2710 | (11) 98765-4120</p>
      <p>contato@brunoroarq.com.br</p>
    </address>

    <div class="signature" role="img" aria-label="Assinatura manuscrita de Mariana Forteso"></div>
    <svg class="seal" viewBox="0 0 68 68" aria-hidden="true">
      <circle cx="34" cy="34" r="32" fill="none" stroke="var(--ink-faint)" stroke-width="1.2"/>
    </svg>
  </main>
</body>
</html>
```